Gobal construction supply company needs new business card design

I need a business card design for my global supply company using an existing logo. i will be looking to print these on rounded corner cards with the black background version of my logo on the back. on the front white background, my logo again and my simple details.

```html
<!DOCTYPE html>
<html lang="en">
<head>
<meta charset="utf-8">
<title>Meridian Build Supply – Business Card</title>
<link href="https://fonts.googleapis.com/css2?family=Roboto:wght@400;500;700&display=swap" rel="stylesheet">
<style>
  :root {
    --backdrop: #b9b9b9;
    --card-dark: #1b1b1b;
    --card-light: #f3f3f3;
    --ink: #111111;
    --ink-soft: #4a4a4a;
    --accent: #d90000;
    --white: #f4f4f4;
  }
  * { box-sizing: border-box; margin: 0; padding: 0; }
  html, body {
    width: 1200px;
    height: 960px;
    overflow: hidden;
    background: var(--backdrop);
    font-family: "Roboto", Arial, sans-serif;
  }
  .canvas { position: relative; width: 1200px; height: 960px; }

  .card {
    position: absolute;
    left: 300px;
    width: 600px;
    height: 343px;
    border-radius: 22px;
    overflow: hidden;
  }
  .card--back { top: 122px; background: var(--card-dark); }
  .card--front { top: 495px; background: var(--card-light); }

  /* Back: brand lockup */
  .brand-lockup {
    position: absolute;
    left: 0; right: 0;
    top: 104px;
    display: flex;
    flex-direction: column;
    align-items: center;
    gap: 22px;
  }
  .brand-dot {
    width: 24px; height: 24px;
    border-radius: 50%;
    background: var(--accent);
  }
  .brand-name--back {
    color: var(--white);
    font-weight: 500;
    font-size: 22px;
    letter-spacing: 0.5px;
    text-transform: uppercase;
  }

  /* Front: holder */
  .holder {
    position: absolute;
    right: 47px;
    top: 52px;
    text-align: right;
  }
  .holder__name {
    font-weight: 700;
    font-size: 22px;
    color: var(--ink);
    line-height: 1;
  }
  .holder__title {
    margin-top: 4px;
    font-weight: 500;
    font-size: 14.5px;
    color: var(--accent);
    text-transform: uppercase;
  }
  .edge-tab {
    position: absolute;
    right: 0; top: 54px;
    width: 14px; height: 38px;
    background: var(--accent);
  }

  .brand-mark--front {
    position: absolute;
    left: 45px;
    top: 196px;
    display: flex;
    align-items: center;
    gap: 12px;
  }
  .brand-square {
    width: 22px; height: 22px;
    background: var(--accent);
  }
  .brand-name--front {
    color: var(--ink);
    font-weight: 700;
    font-size: 30px;
    line-height: 1.05;
    text-transform: uppercase;
  }

  .address {
    position: absolute;
    right: 47px;
    top: 217px;
    text-align: right;
    font-size: 14.5px;
    line-height: 19px;
    color: var(--ink-soft);
  }
  .rule {
    position: absolute;
    left: 45px; right: 0;
    top: 273px;
    height: 2px;
    background: var(--ink);
  }
  .contact-line {
    position: absolute;
    left: 47px;
    top: 284px;
    font-size: 14.5px;
    color: var(--ink-soft);
  }
</style>
</head>
<body>
<main class="canvas">
  <section class="card card--back" aria-label="Card back">
    <div class="brand-lockup">
      <span class="brand-dot"></span>
      <p class="brand-name--back">Meridian Build Supply</p>
    </div>
  </section>

  <section class="card card--front" aria-label="Card front">
    <div class="holder">
      <p class="holder__name">DANIEL REYES</p>
      <p class="holder__title">CEO/Founder</p>
    </div>
    <span class="edge-tab"></span>

    <div class="brand-mark--front">
      <p class="brand-name--front">Meridian<br>Build Supply</p>
      <span class="brand-square"></span>
    </div>

    <address class="address" style="font-style:normal">
      2319 Cedar Ridge Road<br>
      Fairbanks, Alaska 99701
    </address>

    <div class="rule"></div>
    <p class="contact-line">Ph.555 204 7719 | daniel@meridianbuild.com | meridianbuild.com</p>
  </section>
</main>
</body>
</html>
```